Shabby Shic / Elegant - Web branding and elements needed

Just need a design that has all elements I will need to build out an existing template. Attaching designs that we like and want to be similar in feel to... Also attaching the barebones current template that I need to add the elements to. Anything on there can be modified, just using it for layout so you can use that as a template. In addition, feel free to play with the logo to see if there is a diffrent styl (Perhaps a more flat style).

Target Market(s)

Middle age woman, grandmothers, mothers

Industry/Entity Type

Fashion

Number of Pages Required

3 page

Font styles to use
Sans Serif
Decorative
Script

Colors

Designer to choose colors to be used in the design.

Requirements
Must have
• Easy to see. Fits with demographic.
Should not have
• Just standard, corporate feel

```html
<!DOCTYPE html>
<html lang="en">
<head>
<meta charset="utf-8">
<title>Clara Monogram Font – Stitchbloom</title>
<link href="https://fonts.googleapis.com/css2?family=Open+Sans:wght@400;600;700&family=Roboto+Condensed:wght@700&display=swap" rel="stylesheet">
<style>
:root{
  --pink:#ee3d8f;
  --pink-soft:#ff9ccb;
  --green:#6cc04a;
  --green-soft:#a9e063;
  --yellow:#f7d51d;
  --orange:#f47c20;
  --ink:#333;
  --muted:#666;
  --line:#ddd;
  --page:#f2f6f6;
  --footer:#1e1e1e;
}
*{box-sizing:border-box;margin:0;padding:0}
html,body{width:1088px;height:1200px;overflow:hidden}
body{position:relative;font-family:"Open Sans",sans-serif;color:var(--ink);background:var(--page)}
.abs{position:absolute}

.site-header{position:absolute;left:0;top:0;width:1088px;height:99px;background:#fff}
.brand{position:absolute;left:68px;top:36px;display:flex;align-items:center;gap:8px;font-size:26px;font-weight:700;color:var(--pink);letter-spacing:.5px}
.brand-dot{width:14px;height:14px;border-radius:50%;background:var(--green)}
.account-links{position:absolute;right:84px;top:19px;font-size:10.5px;letter-spacing:.5px;color:var(--ink)}
.account-links span{margin:0 6px;color:#999}
.search{position:absolute;left:557px;top:46px;width:336px;height:36px;border:1px solid #ccc;border-radius:2px;font-size:12.5px;color:#555;padding:9px 12px}
.search-btn{position:absolute;right:0;top:0;width:48px;height:34px;background:#222;display:flex;align-items:center;justify-content:center}
.cart-btn{position:absolute;left:907px;top:46px;width:35px;height:36px;background:var(--green);border-radius:2px;display:flex;align-items:center;justify-content:center}
.cart-label{position:absolute;left:951px;top:56px;font-size:12px;font-weight:600;color:var(--ink)}
.cart-label b{color:var(--pink);font-weight:400}

.main-nav{position:absolute;left:0;top:99px;width:1088px;height:49px;background:var(--pink);display:flex;justify-content:center;align-items:center;gap:17px;font-family:"Roboto Condensed",sans-serif;font-size:11.6px;color:#fff;letter-spacing:.2px}
.main-nav::before,.main-nav::after{content:"";position:absolute;left:0;right:0;border-top:1px dashed rgba(255,255,255,.8)}
.main-nav::before{top:3px}.main-nav::after{bottom:3px}

.product-card{position:absolute;left:54px;top:162px;width:980px;height:558px;background:#fff;border-radius:10px;box-shadow:0 0 8px rgba(0,0,0,.12)}
.product-title{position:absolute;left:68px;top:197px;font-size:20px;font-weight:600;letter-spacing:.4px;color:#444}
.product-title em{font-style:normal;font-weight:700;color:var(--pink)}
.gallery-main{position:absolute;left:68px;top:245px;width:464px;height:312px;border:2px solid #e4e4e4;border-radius:10px;background:#fff;padding:12px}
.art{width:100%;height:100%;border-radius:4px;background:linear-gradient(135deg,#fbe3ef 0%,#eef2dd 35%,#dff0fa 60%,#fde7d4 100%)}
.thumb{position:absolute;top:566px;width:149px;height:95px;border:2px solid #e4e4e4;border-radius:9px;padding:10px 18px;background:#fff}

.spec{position:absolute;left:556px;font-size:13px}
.spec dt{position:absolute;left:0;font-weight:700;color:var(--pink);white-space:nowrap}
.spec dd{position:absolute;left:151px;color:var(--ink);white-space:nowrap}
.rule{position:absolute;left:556px;width:452px;border-top:1px solid var(--line)}
.old-price{position:absolute;left:557px;top:372px;font-size:13px;font-weight:600;color:#555}
.old-price s{color:#555}
.price{position:absolute;left:556px;top:390px;font-size:30px;font-weight:700;color:var(--orange)}
.saving{position:absolute;left:557px;top:428px;font-size:14.5px;font-weight:600;color:#333}
.format-label{position:absolute;left:763px;top:372px;font-size:13px;font-weight:600;color:#555}
.format-select{position:absolute;left:763px;top:401px;width:229px;height:35px;border:1px solid #bbb;border-radius:18px;font-size:11.5px;padding:10px 17px;color:#333}
.format-select svg{position:absolute;right:14px;top:12px}
.code{position:absolute;left:556px;top:505px;font-size:13px;font-weight:700;color:var(--pink)}
.code span{margin-left:20px;color:var(--green)}
.note{position:absolute;left:557px;top:550px;font-size:13px;color:#333;letter-spacing:.2px}
.btn-cart{position:absolute;left:557px;top:584px;width:138px;height:40px;background:var(--green);color:#fff;font-size:14px;font-weight:600;letter-spacing:.6px;display:flex;align-items:center;justify-content:center;border-radius:2px}
.wish{position:absolute;left:725px;top:596px;font-size:13px;font-weight:700;color:var(--pink);display:flex;align-items:center;gap:16px;letter-spacing:.4px}

.promo{position:absolute;top:748px;width:299px;height:146px;border-radius:10px;overflow:hidden;color:#fff;text-align:center}
.promo::before{content:"";position:absolute;inset:5px;border:1px dashed rgba(255,255,255,.85);border-radius:8px}
.promo h3{position:absolute;left:0;right:0;top:25px;font-size:26px;font-weight:400;line-height:27px;letter-spacing:.6px}
.promo .btn{position:absolute;left:95px;top:94px;width:110px;height:33px;font-size:11.5px;font-weight:700;letter-spacing:.6px;display:flex;align-items:center;justify-content:center;border-radius:1px}
.promo svg{position:absolute;right:16px;bottom:13px}
.promo-news{left:68px;background:var(--green-soft)}
.promo-news .btn{background:var(--green)}
.promo-cats{left:395px;background:var(--yellow)}
.promo-cats .btn{background:var(--orange)}
.promo-gift{left:721px;background:var(--pink-soft)}
.promo-gift .btn{background:var(--pink)}

.site-footer{position:absolute;left:0;top:957px;width:1088px;height:243px;background:var(--footer);color:#ddd;font-size:11.5px}
.site-footer::before{content:"";position:absolute;left:0;right:0;top:4px;border-top:1px dashed #777}
.footer-brand{position:absolute;left:68px;top:38px;display:flex;align-items:center;gap:8px;font-size:26px;font-weight:700;color:var(--pink)}
.footer-copy{position:absolute;left:68px;top:114px;line-height:19px;width:220px}
.footer-copy p+p{margin-top:7px}
.footer-col{position:absolute;top:36px}
.footer-col h4{font-size:13px;font-weight:700;color:var(--green);letter-spacing:.5px;margin-bottom:6px}
.footer-col li{list-style:none;line-height:25px}
.social{position:absolute;left:804px;top:155px;display:flex;gap:15px}
.social span{width:15px;height:15px;border-radius:50%;background:#eee}
</style>
</head>
<body>

<header class="site-header">
  <div class="brand"><span class="brand-dot"></span>stitchbloom</div>
  <nav class="account-links">LOG IN<span>|</span>REGISTER<span>|</span>WISHLIST<span>|</span>CHECKOUT</nav>
  <div class="search">Search..
    <div class="search-btn"><svg width="14" height="14" viewBox="0 0 14 14"><circle cx="6" cy="6" r="4.5" fill="none" stroke="#fff" stroke-width="2"/><line x1="9.3" y1="9.3" x2="13" y2="13" stroke="#fff" stroke-width="2.2"/></svg></div>
  </div>
  <div class="cart-btn"><svg width="15" height="13" viewBox="0 0 15 13"><path d="M0 1h3l2 7h8l2-5H4.5" fill="none" stroke="#fff" stroke-width="1.8"/><circle cx="6" cy="11" r="1.4" fill="#fff"/><circle cx="12" cy="11" r="1.4" fill="#fff"/></svg></div>
  <div class="cart-label">MY CART <b>(0)</b></div>
</header>

<nav class="main-nav">
  <span>NEW RELEASE</span><span>FEATURED PRODUCTS</span><span>ACCENTS</span><span>ALPHABETS &amp; LETTERING</span><span>APPLIQUE</span><span>FONT FRAMES</span><span>IN THE HOOP</span><span>WORDS &amp; PHRASE</span><span>SEWING PATTERNS</span><span>OTHER CATEGORIES</span>
</nav>

<section class="product-card"></section>
<h1 class="product-title">CLARA MONOGRAM FONT <em>- ELEGANT SCRIPT FONT</em></h1>

<div class="gallery-main"><div class="art" role="img" aria-label="Sample names stitched in the elegant script font in pink, green, blue and orange"></div></div>
<div class="thumb" style="left:68px"><div class="art" role="img" aria-label="Thumbnail of stitched name samples"></div></div>
<div class="thumb" style="left:226px"><div class="art" style="background:linear-gradient(135deg,#f4f1fa,#eaeef8)" role="img" aria-label="Thumbnail of the full alphabet chart"></div></div>
<div class="thumb" style="left:383px"><div class="art" style="background:linear-gradient(135deg,#f7e4f0,#def0fa)" role="img" aria-label="Thumbnail of a three letter monogram"></div></div>

<dl class="spec" style="top:242px"><dt>Description:</dt><dd>Aa-Zz, 0-9, punctuation</dd></dl>
<dl class="spec" style="top:272px"><dt>Sizes Included:</dt><dd>0.5", 1", 1.5", 2", 2.5", 3"</dd></dl>
<dl class="spec" style="top:302px"><dt>Design Dimensions:</dt><dd>(0.55" x 0.52"), (0.96" x 1.03"), (1.56" x 1.46"),...</dd></dl>
<div class="rule" style="top:348px"></div>

<div class="old-price">Old price: <s>$7.49</s></div>
<div class="price">$3.74</div>
<div class="saving">You save: $3.75 (50%)</div>
<div class="format-label">File Format:</div>
<div class="format-select">Select Format:
  <svg width="7" height="10" viewBox="0 0 7 10"><path d="M0 4L3.5 0 7 4zM0 6l3.5 4L7 6z" fill="#333"/></svg>
</div>
<div class="rule" style="top:472px"></div>

<div class="code">Code: <span>stbmclara</span></div>
<p class="note">This product is electronically distributed.</p>
<div class="btn-cart">ADD TO CART</div>
<div class="wish"><svg width="14" height="12" viewBox="0 0 14 12"><path d="M7 12L1.2 6.2A3.4 3.4 0 0 1 7 1.8a3.4 3.4 0 0 1 5.8 4.4z" fill="#ee3d8f"/></svg>ADD TO WISH LIST</div>

<div class="promo promo-news">
  <h3>SIGN UP<br>NEWSLETTER</h3><div class="btn">SUBSCRIBE</div>
  <svg width="64" height="50" viewBox="0 0 64 50"><rect x="1" y="1" width="62" height="48" rx="4" fill="#fff" opacity=".55"/><path d="M3 4l29 24L61 4" fill="none" stroke="#a9e063" stroke-width="4"/></svg>
</div>
<div class="promo promo-cats">
  <h3>SHOP BY<br>CATEGORIES</h3><div class="btn">SHOP NOW</div>
  <svg width="68" height="54" viewBox="0 0 68 54"><path d="M2 4h26l30 26-22 22L6 26z" fill="#fff" opacity=".6"/><circle cx="15" cy="15" r="4" fill="#f7d51d"/><path d="M34 4l30 26-22 22" fill="none" stroke="#fff" stroke-width="4" opacity=".6"/></svg>
</div>
<div class="promo promo-gift">
  <h3>GIFT<br>CERTIFICATES</h3><div class="btn">SHOP NOW</div>
  <svg width="58" height="50" viewBox="0 0 58 50"><g fill="#fff" opacity=".6"><rect x="2" y="14" width="54" height="12"/><rect x="6" y="28" width="46" height="22"/><path d="M29 13c-6-12-18-12-16-4 1 4 10 4 16 4zM29 13c6-12 18-12 16-4-1 4-10 4-16 4z"/></g><rect x="26" y="14" width="6" height="36" fill="#ff9ccb"/></svg>
</div>

<footer class="site-footer">
  <div class="footer-brand"><span class="brand-dot"></span>stitchbloom</div>
  <div class="footer-copy">
    <p>Copyright © 2017. Stitchbloom<br>All Right Reserved</p>
    <p>Stitchbloom is a registered trademark of Stitchbloom, LLC. All text, images and designs</p>
  </div>
  <div class="footer-col" style="left:346px"><h4>NAVIGATION</h4><ul><li>Home</li><li>About Us</li><li>Products</li><li>Services</li><li>Contact Us</li></ul></div>
  <div class="footer-col" style="left:565px"><h4>MY ACCOUNT</h4><ul><li>Register</li><li>Log In</li><li>My Cart</li><li>Checkout</li><li>Wishlist</li></ul></div>
  <div class="footer-col" style="left:804px"><h4>LEGAL</h4><ul><li>Terms and Conditions</li><li>Privacy Policy</li><li>Refund Policy</li></ul></div>
  <div class="social" aria-label="Social links"><span></span><span></span><span></span><span></span><span></span></div>
</footer>

</body>
</html>
```